Training Company Needs a Web Design

We are a Training company that needs a website design completed for us. "The Harbor Loft" The website will be a 'community space' specialising in 'Change and Transformation'. It will be a 'space' where individuals can come to find out 'latest news', upcoming events and courses, chat with others and find 'tools and templates'. They will need to login as a 'Member'.

The final design needs to be professional but have a 'fun and interactive' feel and appeal to our target audience who are predominantly corporate individuals.

Target Market(s)

Corporate Individuals - they may have a Change or Project background

Industry/Entity Type

Business Consultant

Number of Pages Required

3 page

Font styles to use
Sans Serif

Requirements
Must have
• Design for 'Home Page'
• A professional and corporate 'feel' but be fun and interactive.
Nice to have
• A 'sense' of how some of the other pages may be designed or laid out.

```html
<!DOCTYPE html>
<html lang="en">
<head>
<meta charset="utf-8">
<title>The Harbor Loft – Home</title>
<link href="https://fonts.googleapis.com/css2?family=Open+Sans:ital,wght@0,400;0,600;0,700;1,700&display=swap" rel="stylesheet">
<style>
:root{
  --frame:#e6e7e8;
  --navy:#0c4f8b;
  --navy-deep:#0a3b63;
  --teal:#4ad8bf;
  --teal-dark:#2bbfa7;
  --ink:#1b1b1b;
  --label:#174f82;
  --body:#333;
  --orange:#e8573a;
  --yellow:#f1c83b;
  --cyan:#1ba4dd;
  --blue:#1d5b95;
  --purple:#8f6cb1;
  --white:#fff;
}
*{box-sizing:border-box;margin:0;padding:0}
html,body{width:1200px;height:2880px;overflow:hidden;background:var(--frame);font-family:"Open Sans",Arial,sans-serif;color:var(--ink)}
.page{position:absolute;left:17px;top:15px;width:1166px;height:2823px;background:var(--white);overflow:hidden;border-top:5px solid var(--teal)}
.abs{position:absolute}

/* header */
.brand{left:45px;top:28px;display:flex;align-items:center;gap:16px}
.brand-dot{width:46px;height:46px;border-radius:50%;background:var(--cyan)}
.brand-name{color:var(--cyan);font-weight:400;font-size:31px;line-height:32px;text-transform:uppercase}
.auth{right:30px;top:13px;display:flex;gap:9px}
.btn-auth{width:150px;height:32px;border-radius:16px;color:#fff;font-weight:700;font-size:15px;display:flex;align-items:center;justify-content:center;border:2px solid var(--navy-deep)}
.btn-signup{background:var(--navy)}
.btn-login{background:#1589ad}
.consult{right:30px;top:80px;display:flex;align-items:center;gap:12px}
.consult-label{font-size:16px;font-weight:700;color:#222;letter-spacing:-.2px}
.consult-number{font-size:33px;line-height:34px;font-weight:600;color:var(--teal-dark)}

/* nav */
.nav{left:0;top:147px;width:1166px;height:48px;background:linear-gradient(#11589a,#0c4679)}
.nav a{position:absolute;top:13px;color:#fff;text-decoration:none;font-size:16px;font-weight:600;text-transform:uppercase}
.nav a.active{color:var(--teal)}

/* hero */
.hero-photo{left:0;top:195px;width:1166px;height:620px;background:linear-gradient(135deg,#c7d6e0 0%,#8fa8bb 35%,#5d7f99 60%,#2f4f6b 100%)}
.hero-caption{left:0;top:603px;width:1166px;height:120px;background:rgba(74,216,191,.45);color:#fff;font-size:29px;line-height:38px;text-align:center;padding-top:22px}
.pillars{left:0;top:752px;width:1166px;height:200px}
.pillar{position:absolute;top:0;width:160px;text-align:center}
.pillar-disc{width:134px;height:134px;margin:0 auto;border-radius:50%;border:5px solid #fff;box-shadow:0 3px 8px rgba(0,0,0,.3);display:flex;align-items:center;justify-content:center}
.pillar-name{margin-top:12px;font-size:19px;font-weight:700;color:var(--label);text-transform:uppercase}

/* what is */
.about{left:0;top:955px;width:1166px;height:320px}
.about-title{left:40px;top:125px;color:#fff;font-size:22px;line-height:27px;font-weight:700;text-transform:uppercase}
.about-text{left:395px;top:60px;width:340px;color:#fff;font-size:16px;line-height:25px;font-weight:600}
.btn-dark{background:var(--navy-deep);color:#fff;font-size:15px;font-weight:700;text-transform:uppercase;display:flex;align-items:center;justify-content:center;border-radius:4px;box-shadow:0 2px 3px rgba(0,0,0,.35)}
.about-btn{left:473px;top:227px;width:144px;height:44px}
.video{left:755px;top:43px;width:360px;height:236px;border:4px solid #fff;border-radius:4px;background:linear-gradient(160deg,#8a8f86,#5e6b63 50%,#3f4b4a)}
.video-play{left:145px;top:83px}

/* features */
.features-title{left:0;top:1328px;width:1166px;text-align:center;font-size:23px;font-weight:700}
.features-intro{left:0;top:1370px;width:1166px;text-align:center;font-size:15px;font-weight:600;color:#222}
.feature{position:absolute;top:1408px;width:180px;text-align:center}
.feature-name{margin-top:10px;font-size:16px;line-height:23px;font-weight:700;color:var(--label);text-transform:uppercase}

/* testimonials */
.testimonials{left:0;top:1655px;width:1166px;height:320px}
.avatar{left:28px;top:60px;width:112px;height:112px;border-radius:50%;border:4px solid #2a9fd0;background:linear-gradient(#8a6a55,#4a3427)}
.avatar-tip{left:138px;top:98px}
.quote{left:213px;top:45px;width:520px;color:#fff;font-size:15px;line-height:24px}
.quote-author{left:213px;top:195px;color:#fff;font-size:17px;font-weight:700;font-style:italic}
.testimonials-title{left:920px;top:145px;color:#fff;font-size:21px;font-weight:700;text-transform:uppercase}
.dots{left:440px;top:272px;display:flex;gap:8px}
.dots i{width:11px;height:11px;border-radius:50%;background:#fff}
.dots i.on{background:var(--cyan)}

/* blog */
.blog-title{left:0;top:2030px;width:1166px;text-align:center;font-size:23px;font-weight:700}
.post{position:absolute;top:2074px;width:351px}
.post-photo{width:351px;height:234px}
.date{position:absolute;left:18px;top:18px;width:76px}
.date-top{background:var(--navy);color:#fff;text-align:center;padding:6px 0 2px;font-weight:700;line-height:20px}
.date-day{font-size:27px;display:block;line-height:28px}
.date-month{font-size:14px}
.date-year{background:#fff;text-align:center;font-size:15px;font-weight:700;color:#333;padding:3px 0}
.post-title{margin-top:24px;font-size:19px;font-weight:700}
.post-text{margin-top:8px;font-size:15px;line-height:23px;color:var(--body)}
.post-btn{margin-top:22px;width:146px;height:46px}

/* footer */
.footer{left:0;top:2534px;width:1166px;height:261px}
.footer-brand{left:40px;top:92px;display:flex;align-items:center;gap:14px}
.footer-head{color:var(--teal);font-size:14px;font-weight:700;text-transform:uppercase}
.footer-links a{display:block;color:#fff;text-decoration:none;font-size:12px;font-weight:700;line-height:20px;text-transform:uppercase}
.field{width:218px;height:30px;background:var(--navy-deep);color:#fff;font-size:13px;padding:6px 10px;margin-bottom:3px}
.field-msg{height:66px}
.send{width:110px;height:38px;background:#111;border:2px solid #ccc;color:#fff;font-weight:700;font-size:15px;display:flex;align-items:center;justify-content:center;margin-top:6px}
.contact-row{display:flex;gap:10px;color:#fff;font-size:12px;font-weight:700;line-height:18px;text-transform:uppercase}
.copyright{left:0;top:2795px;width:1166px;height:25px;background:var(--teal);text-align:center;font-size:10px;font-weight:700;color:var(--navy-deep);line-height:25px;text-transform:uppercase}
</style>
</head>
<body>
<div class="page">

  <header>
    <div class="abs brand">
      <span class="brand-dot"></span>
      <span class="brand-name">The<br>Harbor<br>Loft</span>
    </div>
    <div class="abs auth">
      <span class="btn-auth btn-signup">SIGN UP</span>
      <span class="btn-auth btn-login">LOGIN</span>
    </div>
    <div class="abs consult">
      <svg width="44" height="44" viewBox="0 0 44 44"><circle cx="22" cy="22" r="19" fill="none" stroke="#2bbfa7" stroke-width="3"/><path d="M15 12c2-1 3 0 4 3s0 3-1 4c1 3 3 5 6 6 1-1 2-2 4-1s4 2 3 4-3 3-5 3C17 31 12 25 12 18c0-3 1-5 3-6z" fill="#2bbfa7"/></svg>
      <div>
        <div class="consult-label">CALL FOR A FREE CONSULTATION</div>
        <div class="consult-number">888.555.0142</div>
      </div>
    </div>
  </header>

  <nav class="abs nav">
    <a class="active" style="left:100px">Home</a>
    <a style="left:227px">What is The Harbor Loft</a>
    <a style="left:528px">Features</a>
    <a style="left:678px">Testimonials</a>
    <a style="left:866px">Blog</a>
    <a style="left:983px">Contact</a>
  </nav>

  <section>
    <div class="abs hero-photo" role="img" aria-label="Photo of four smiling business colleagues talking in an office"></div>
    <p class="abs hero-caption">A unique destination for everything that practitioners need to execute best<br>practice change management, transformation and project methodologies.</p>
    <div class="abs pillars">
      <div class="pillar" style="left:122px">
        <div class="pillar-disc" style="background:var(--orange)">
          <svg width="70" height="70" viewBox="0 0 70 70" fill="#fff" stroke="#fff" stroke-width="4"><line x1="35" y1="35" x2="35" y2="10"/><line x1="35" y1="35" x2="12" y2="28"/><line x1="35" y1="35" x2="58" y2="28"/><line x1="35" y1="35" x2="20" y2="58"/><line x1="35" y1="35" x2="50" y2="58"/><circle cx="35" cy="35" r="8"/><circle cx="35" cy="10" r="5"/><circle cx="12" cy="28" r="5"/><circle cx="58" cy="28" r="5"/><circle cx="20" cy="58" r="5"/><circle cx="50" cy="58" r="5"/></svg>
        </div>
        <div class="pillar-name">Dynamic</div>
      </div>
      <div class="pillar" style="left:312px">
        <div class="pillar-disc" style="background:var(--yellow)">
          <svg width="70" height="70" viewBox="0 0 70 70" fill="#fff"><path d="M8 12h36v24H22l-8 8v-8H8z"/><path d="M30 30h32v24h-6v8l-8-8H30z" stroke="#f1c83b" stroke-width="3"/></svg>
        </div>
        <div class="pillar-name">Personal</div>
      </div>
      <div class="pillar" style="left:502px">
        <div class="pillar-disc" style="background:var(--cyan)">
          <svg width="74" height="70" viewBox="0 0 74 70" fill="#fff"><path d="M4 14c12-4 24-2 31 4v42c-7-5-19-7-31-4z"/><path d="M70 14c-12-4-24-2-31 4v42c7-5 19-7 31-4z"/><g stroke="#1ba4dd" stroke-width="2"><line x1="10" y1="26" x2="29" y2="28"/><line x1="10" y1="34" x2="29" y2="36"/><line x1="10" y1="42" x2="29" y2="44"/><line x1="45" y1="28" x2="64" y2="26"/><line x1="45" y1="36" x2="64" y2="34"/><line x1="45" y1="44" x2="64" y2="42"/></g></svg>
        </div>
        <div class="pillar-name">Learning</div>
      </div>
      <div class="pillar" style="left:692px">
        <div class="pillar-disc" style="background:var(--blue)">
          <svg width="70" height="70" viewBox="0 0 70 70" fill="none" stroke="#fff" stroke-width="7" stroke-linecap="round"><path d="M30 40l-8 8a8 8 0 0 1-11-11l8-8"/><path d="M40 30l8-8a8 8 0 0 0-11-11l-8 8"/><line x1="27" y1="43" x2="43" y2="27"/></svg>
        </div>
        <div class="pillar-name">Connected</div>
      </div>
      <div class="pillar" style="left:882px">
        <div class="pillar-disc" style="background:var(--purple)">
          <svg width="70" height="70" viewBox="0 0 70 70" fill="#fff"><line x1="20" y1="35" x2="50" y2="18" stroke="#fff" stroke-width="4"/><line x1="20" y1="35" x2="50" y2="52" stroke="#fff" stroke-width="4"/><circle cx="20" cy="35" r="9"/><circle cx="50" cy="18" r="9"/><circle cx="50" cy="52" r="9"/></svg>
        </div>
        <div class="pillar-name">Vibrant</div>
      </div>
    </div>
  </section>

  <section class="abs about">
    <svg class="abs" style="left:0;top:0" width="1166" height="320"><rect width="1166" height="320" fill="#0c4f8b"/><polygon points="0,0 378,0 240,320 0,320" fill="#4ad8bf"/></svg>
    <h2 class="abs about-title">What is<br>The Harbor Loft</h2>
    <p class="abs about-text">The Harbor Loft's offering will be positioned as a place of learning, connecting, collaborating and sharing. It's a resource for change professional to further the conversation around change.</p>
    <span class="abs btn-dark about-btn">Read More</span>
    <div class="abs video" role="img" aria-label="Video still of a group seated in a circle at a workshop">
      <svg class="abs video-play" width="62" height="62" viewBox="0 0 62 62"><circle cx="31" cy="31" r="30" fill="rgba(0,0,0,.55)" stroke="#fff" stroke-width="2"/><path d="M24 18l22 13-22 13z" fill="#fff"/></svg>
    </div>
  </section>

  <section>
    <h2 class="abs features-title">FEATURES</h2>
    <p class="abs features-intro">The Harbor Loft is a 'community' whereby an individual can go to learn, connect, collaborate and share, where you will be able to</p>

    <div class="feature" style="left:20px">
      <svg width="130" height="124" viewBox="10 10 130 124"><circle cx="75" cy="72" r="56" fill="none" stroke="#2bbfa7" stroke-width="7"/><circle cx="75" cy="58" r="15" fill="#1d5b95"/><path d="M47 106c0-18 12-28 28-28s28 10 28 28z" fill="#1d5b95"/></svg>
      <div class="feature-name">Upload your<br>profile</div>
    </div>
    <div class="feature" style="left:201px">
      <svg width="130" height="124" viewBox="10 10 130 124"><circle cx="75" cy="72" r="56" fill="none" stroke="#2bbfa7" stroke-width="7"/><rect x="56" y="44" width="38" height="58" fill="none" stroke="#1d5b95" stroke-width="4"/><rect x="66" y="38" width="18" height="10" fill="#1d5b95"/><g stroke="#1d5b95" stroke-width="3"><path d="M62 60l3 3 5-6M62 76l3 3 5-6M62 92l3 3 5-6" fill="none"/><line x1="74" y1="60" x2="88" y2="60"/><line x1="74" y1="76" x2="88" y2="76"/><line x1="74" y1="92" x2="88" y2="92"/></g></svg>
      <div class="feature-name">Gain access to<br>training<br>information</div>
    </div>
    <div class="feature" style="left:382px">
      <svg width="130" height="124" viewBox="10 10 130 124"><circle cx="75" cy="72" r="56" fill="none" stroke="#2bbfa7" stroke-width="7"/><rect x="58" y="42" width="34" height="20" fill="none" stroke="#1d5b95" stroke-width="3"/><g fill="#1d5b95"><circle cx="54" cy="76" r="5"/><circle cx="68" cy="76" r="5"/><circle cx="82" cy="76" r="5"/><circle cx="96" cy="76" r="5"/><circle cx="47" cy="94" r="5"/><circle cx="61" cy="94" r="5"/><circle cx="75" cy="94" r="5"/><circle cx="89" cy="94" r="5"/><circle cx="103" cy="94" r="5"/></g></svg>
      <div class="feature-name">Upcoming events,<br>speakers &amp;<br>webinars</div>
    </div>
    <div class="feature" style="left:563px">
      <svg width="130" height="124" viewBox="10 10 130 124"><circle cx="75" cy="72" r="56" fill="none" stroke="#2bbfa7" stroke-width="7"/><circle cx="75" cy="72" r="22" fill="none" stroke="#1d5b95" stroke-width="7" stroke-dasharray="8 5"/><circle cx="75" cy="72" r="10" fill="none" stroke="#1d5b95" stroke-width="4"/></svg>
      <div class="feature-name">Access to<br>tools &amp;<br>templates</div>
    </div>
    <div class="feature" style="left:744px">
      <svg width="130" height="124" viewBox="10 10 130 124"><circle cx="75" cy="72" r="56" fill="none" stroke="#2bbfa7" stroke-width="7"/><path d="M50 48h50v34H76l-12 12V82H50z" fill="none" stroke="#1d5b95" stroke-width="4"/><path d="M75 54l4 8 8 1-6 5 2 8-8-4-8 4 2-8-6-5 8-1z" fill="#1d5b95"/></svg>
      <div class="feature-name">Gain further<br>accreditation</div>
    </div>
    <div class="feature" style="left:925px">
      <svg width="130" height="124" viewBox="10 10 130 124"><circle cx="75" cy="72" r="56" fill="none" stroke="#2bbfa7" stroke-width="7"/><g fill="#1d5b95"><rect x="50" y="84" width="16" height="18"/><rect x="68" y="70" width="16" height="32"/><rect x="86" y="54" width="16" height="48"/><circle cx="76" cy="52" r="5"/><rect x="70" y="60" width="12" height="8"/></g></svg>
      <div class="feature-name">Get access<br>to coaching</div>
    </div>
  </section>

  <section class="abs testimonials">
    <svg class="abs" style="left:0;top:0" width="1166" height="320"><rect width="1166" height="320" fill="#4ad8bf"/><polygon points="0,0 790,0 940,320 0,320" fill="#0c4f8b"/></svg>
    <div class="abs avatar" role="img" aria-label="Portrait of the reviewer"></div>
    <svg class="abs avatar-tip" width="20" height="36" viewBox="0 0 20 36"><path d="M0 0l18 18L0 36z" fill="#2a9fd0"/></svg>
    <svg class="abs" style="left:170px;top:45px" width="40" height="30" viewBox="0 0 40 30" fill="#1ba4dd"><path d="M0 0h16v16l-8 14H2l6-14H0zM22 0h16v16l-8 14h-6l6-14h-8z"/></svg>
    <p class="abs quote">Lorem ipsum dolor sit amet, consectetuer adipiscing elit, sed diam nonummy nibh euismod tincidunt ut laoreet dolore magna aliquam erat volutpat. Ut wisi enim ad minim veniam, quis nostrud exercitat ion ullamcorper suscipit lobortis nisl ut aliquip ex ea commodo conse quat. Duis autem vel eum iriure dolor in hendrerit in vulputate velit.</p>
    <svg class="abs" style="left:765px;top:145px" width="40" height="30" viewBox="0 0 40 30" fill="#1ba4dd"><path d="M0 0h16v16l-8 14H2l6-14H0zM22 0h16v16l-8 14h-6l6-14h-8z"/></svg>
    <p class="abs quote-author">Maya R</p>
    <h2 class="abs testimonials-title">Testimonials</h2>
    <div class="abs dots"><i class="on"></i><i></i><i></i></div>
  </section>

  <section>
    <h2 class="abs blog-title">LATEST FROM THE BLOG</h2>
    <article class="post" style="left:29px">
      <div class="post-photo" role="img" aria-label="Photo of colleagues laughing around a laptop" style="background:linear-gradient(135deg,#e6ecf1,#b8c6d2 50%,#7b8c99)"></div>
      <div class="date"><div class="date-top"><span class="date-day">01</span><span class="date-month">SEP</span></div><div class="date-year">2015</div></div>
      <h3 class="post-title">Blog Post #1</h3>
      <p class="post-text">Lorem ipsum dolor sit amet, consectetuer adipisci elit, sed diam nonummy nibh euismod tincidunt ut laoreet dolore magna aliquam erat volutpat.</p>
      <span class="btn-dark post-btn">Read More</span>
    </article>
    <article class="post" style="left:407px">
      <div class="post-photo" role="img" aria-label="Photo of city skyscrapers at dusk" style="background:linear-gradient(160deg,#7d94b8,#3d4f74 50%,#1a2236)"></div>
      <div class="date"><div class="date-top"><span class="date-day">01</span><span class="date-month">SEP</span></div><div class="date-year">2015</div></div>
      <h3 class="post-title">Blog Post #2</h3>
      <p class="post-text">Lorem ipsum dolor sit amet, consectetuer adipisci elit, sed diam nonummy nibh euismod tincidunt ut laoreet dolore magna aliquam erat volutpat.</p>
      <span class="btn-dark post-btn">Read More</span>
    </article>
    <article class="post" style="left:787px">
      <div class="post-photo" role="img" aria-label="Photo of a speaker presenting to a seated audience" style="background:linear-gradient(180deg,#f2f4f6,#d2d9df 55%,#8d99a4)"></div>
      <div class="date"><div class="date-top"><span class="date-day">01</span><span class="date-month">SEP</span></div><div class="date-year">2015</div></div>
      <h3 class="post-title">Blog Post #3</h3>
      <p class="post-text">Lorem ipsum dolor sit amet, consectetuer adipisci elit, sed diam nonummy nibh euismod tincidunt ut laoreet dolore magna aliquam erat volutpat.</p>
      <span class="btn-dark post-btn">Read More</span>
    </article>
  </section>

  <footer class="abs footer">
    <svg class="abs" style="left:0;top:0" width="1166" height="261"><rect width="1166" height="261" fill="#0c4f8b"/><polygon points="0,0 378,0 232,261 0,261" fill="#fff"/></svg>
    <div class="abs footer-brand">
      <span class="brand-dot" style="width:38px;height:38px"></span>
      <span class="brand-name" style="font-size:26px;line-height:27px">The<br>Harbor<br>Loft</span>
    </div>
    <div class="abs" style="left:385px;top:20px">
      <div class="footer-head" style="margin-bottom:10px">Navigation</div>
      <nav class="footer-links"><a>Home</a><a>What is The Harbor Loft</a><a>Features</a><a>Blog</a><a>Contact</a></nav>
    </div>
    <div class="abs" style="left:625px;top:20px">
      <div class="footer-head" style="margin-bottom:10px">Quick Contact</div>
      <div class="field">Name</div>
      <div class="field">Email</div>
      <div class="field">Phone</div>
      <div class="field field-msg">Message</div>
      <div class="send">SEND</div>
    </div>
    <div class="abs" style="left:915px;top:20px">
      <div class="footer-head" style="margin-bottom:12px">Contact</div>
      <div class="contact-row"><svg width="14" height="18" viewBox="0 0 14 18"><path d="M7 0a7 7 0 0 1 7 7c0 5-7 11-7 11S0 12 0 7a7 7 0 0 1 7-7z" fill="#fff"/><circle cx="7" cy="7" r="2.5" fill="#0c4f8b"/></svg><span>The Harbor Loft<br>42 Wharf Lane<br>Hobart, TAS</span></div>
      <div class="contact-row" style="margin-top:22px"><svg width="16" height="14" viewBox="0 0 16 14"><path d="M1 3c0-2 14-2 14 0v2h-4V3H5v2H1zM3 7h10l2 7H1z" fill="#fff"/></svg><span>(888)555-0142</span></div>
      <div class="contact-row" style="margin-top:22px;text-transform:none"><svg width="16" height="12" viewBox="0 0 16 12"><rect width="16" height="12" fill="#fff"/><path d="M0 0l8 6 8-6" fill="none" stroke="#0c4f8b" stroke-width="1.5"/></svg><span>info@theharborloft.com</span></div>
      <div style="display:flex;gap:8px;margin-top:16px"><span style="width:18px;height:18px;border-radius:50%;background:#1ba4dd"></span><span style="width:18px;height:18px;border-radius:50%;background:#1ba4dd"></span></div>
    </div>
  </footer>
  <div class="abs copyright">Copyright © 2016 The Harbor Loft. All rights reserved</div>

</div>
</body>
</html>
```